Oaths and Harbors (Book cover needed)

Oaths and Harbors: Notes from Years of Civic Labor

Author: Lorena Fabbri Okonkwo

Foreword by Ambassador Tessaly R. Brunwick

Book Trim Size: 5.5 x 8.5

```html
<!DOCTYPE html>
<html lang="en">
<head>
<meta charset="UTF-8">
<title>Oaths and Harbors — Book Cover</title>
<link rel="stylesheet" href="https://fonts.googleapis.com/css2?family=Cinzel:wght@400&display=swap">
<style>
  :root {
    --backdrop: #4a4a4a;
    --band-brown: #8f5f2f;
    --rule-white: #ffffff;
    --footer-black: #000000;
    --text-light: #ffffff;
    --photo-top: #c7a391;
    --photo-mid: #a9735c;
    --photo-bottom: #6d3f34;
  }
  html, body {
    margin: 0;
    padding: 0;
    width: 1200px;
    height: 1200px;
    overflow: hidden;
    background: var(--backdrop);
  }
  .canvas {
    position: relative;
    width: 1200px;
    height: 1200px;
  }
  .cover {
    position: absolute;
    left: 276px;
    top: 100px;
    width: 647px;
    height: 1000px;
    display: flex;
    flex-direction: column;
    font-family: "Cinzel", "Trajan Pro", serif;
    color: var(--text-light);
    box-shadow: 0 18px 40px rgba(0,0,0,0.35);
  }
  .cover-photo {
    height: 629px;
    background:
      radial-gradient(ellipse at 55% 45%, rgba(140,40,40,0.35), transparent 55%),
      linear-gradient(180deg, var(--photo-top) 0%, var(--photo-mid) 55%, var(--photo-bottom) 100%);
  }
  .author-band {
    height: 134px;
    background: var(--band-brown);
    display: flex;
    flex-direction: column;
    align-items: center;
    justify-content: center;
    text-align: center;
  }
  .author-name {
    margin: 0;
    font-size: 48px;
    font-weight: 400;
    line-height: 1.02;
    letter-spacing: 1px;
  }
  .band-rule {
    height: 8px;
    background: var(--rule-white);
  }
  .title-band {
    height: 132px;
    background: var(--band-brown);
    display: flex;
    flex-direction: column;
    align-items: center;
    justify-content: center;
    text-align: center;
  }
  .book-title {
    margin: 0;
    font-size: 45px;
    font-weight: 400;
    line-height: 1.05;
    letter-spacing: 1px;
  }
  .book-subtitle {
    margin: 4px 0 0;
    font-size: 25px;
    font-weight: 400;
    letter-spacing: 1.5px;
  }
  .foreword-band {
    flex: 1;
    background: var(--footer-black);
    display: flex;
    align-items: center;
    justify-content: center;
  }
  .foreword-credit {
    margin: 0;
    font-size: 18px;
    letter-spacing: 0.8px;
  }
</style>
</head>
<body>
  <main class="canvas">
    <article class="cover">
      <div class="cover-photo" role="img" aria-label="Portrait photograph of the author, smiling, wearing a red head wrap and a patterned red and black dress, seated in a warmly lit room"></div>
      <header class="author-band">
        <h2 class="author-name">LORENA FABBRI<br>OKONKWO</h2>
      </header>
      <div class="band-rule"></div>
      <section class="title-band">
        <h1 class="book-title">OATHS AND HARBORS:</h1>
        <p class="book-subtitle">NOTES FROM YEARS OF CIVIC LABOR</p>
      </section>
      <footer class="foreword-band">
        <p class="foreword-credit">FOREWORD BY AMBASSADOR TESSALY R. BRUNWICK</p>
      </footer>
    </article>
  </main>
</body>
</html>
```